Wordpress Design for my Consulting Company

We want a WordPress site created for our new business. We have created a mock-up of the content we want on the site at https://marcobellweather.example.com/website-5

We are not attached to any of the pictures and just put stock stuff from bloq's editor, which we don't have rights to use outside of bloq.

We are NOT looking to just port this site to WordPress, we are looking for some creative ways to display the content in a more professional artistic sense.

I have included several logo files and a text file with the colors and Fonts used in the logo. We are not looking to change the logo or the colors used in the logo.

The Schedule appointment links to a page that embeds a bookslot.example calendar. https://bookslot.example.com/marco-bellweather/trailguide

The final website domain will be venturelanterns.example

Venture lanterns is a consulting company that works directly with the business owners and leaders of small businesses between 50-200 employees. We help companies make sure they have the right technology to meet their strategic goals. We are the anti-"Computer Guy" and we focus on business outcomes NOT cool technology gadgets.

The final design should communicate business growth and success.

Target Market(s)

Business Owners of companies with 50-200 employees

Coding

Coded - Design and coding required

Number of Pages Required

1 page

Font styles to use
Serif
Other font styles liked:
• Trajan Pro Bold, Open Sans

Requirements
Must have
• Should focus on consulting rather than technology.
• Should show the customer as the hero and we are just their guide.
• Must use the logo provided and the colors and fonts in the text file provided. Any other colors and fonts must be complementary.
• The design should scale for all devices computer, iPad, or phone
Should not have
• Should not focus on technology, we are the anti-"Computer Guy" and we focus on business outcomes NOT cool technology gadgets.

```html
<!DOCTYPE html>
<html lang="en">
<head>
<meta charset="utf-8">
<title>Venture Lanterns — Technology Advisors</title>
<link rel="stylesheet" href="https://fonts.googleapis.com/css2?family=Cinzel:wght@400;600;700&family=Open+Sans:wght@300;400;600;700&display=swap">
<style>
:root{
  --accent:#c77b4f;
  --accent-dark:#b36a40;
  --slate:#2f3e47;
  --slate-deep:#243139;
  --ink:#3a3a3a;
  --muted:#777;
  --line:#e4e4e4;
  --light:#f4f4f4;
  --white:#fff;
}
*{box-sizing:border-box;margin:0;padding:0}
html,body{width:1200px;height:3321px;overflow:hidden}
body{font-family:"Open Sans",Arial,sans-serif;color:var(--ink);background:var(--white);position:relative}
section,header,footer{position:absolute;left:0;width:1200px}

/* hero */
.hero{top:0;height:600px;overflow:hidden}
.hero-bg{position:absolute;inset:0;background:linear-gradient(120deg,#56626b 0%,#3d4a53 40%,#2b353c 100%)}
.hero-bg::after{content:"";position:absolute;inset:0;background:rgba(30,40,46,.45)}
.brand-tab{position:absolute;left:142px;top:0;width:278px;height:88px;background:var(--white);border-radius:0 0 14px 14px;display:flex;align-items:center;justify-content:center;box-shadow:0 4px 10px rgba(0,0,0,.2)}
.brand-name{font-family:"Cinzel",Georgia,serif;font-size:21px;font-weight:700;color:var(--slate);line-height:1.1;white-space:nowrap}
.main-nav{position:absolute;right:140px;top:0;display:flex}
.main-nav a{display:block;color:var(--white);font-size:12px;text-decoration:none;padding:24px 13px 20px}
.main-nav a.active{background:var(--white);color:var(--accent)}
.hero-copy{position:absolute;left:160px;top:215px;color:var(--white);width:470px}
.hero-copy h1{font-weight:300;font-size:32px;line-height:1.25;letter-spacing:.5px}
.hero-copy p{font-size:17px;line-height:1.45;margin-top:10px}
.btn-pill{display:inline-block;border-radius:20px;font-size:11px;font-weight:700;letter-spacing:.5px;text-transform:uppercase;padding:8px 20px;text-decoration:none}
.hero-copy .btn-pill{background:var(--white);color:var(--accent);margin-top:22px}
.outcomes{position:absolute;left:688px;top:182px;display:grid;grid-template-columns:repeat(3,105px);gap:16px 16px}
.outcome{height:100px;border:1px solid rgba(255,255,255,.55);display:flex;align-items:center;justify-content:center;text-align:center;color:var(--white);font-size:12px;font-weight:700;line-height:1.35;padding:6px;background:rgba(30,40,46,.35)}
.outcome.on{background:var(--white);color:var(--accent);outline:3px solid rgba(255,255,255,.35);outline-offset:3px}
.hero-arrow{position:absolute;top:316px;width:44px;height:26px;display:flex;align-items:center;justify-content:center;color:var(--white);font-size:16px}
.hero-arrow.left{left:0;background:rgba(255,255,255,.18)}
.hero-arrow.right{right:0;background:var(--accent)}
.dots{position:absolute;left:0;right:0;top:532px;display:flex;justify-content:center;gap:8px}
.dots span{width:7px;height:7px;border-radius:50%;background:var(--white)}
.dots span:first-child{width:22px;border-radius:4px}

/* tired */
.tired{top:600px;height:341px}
.section-title{text-align:center;font-family:"Cinzel",Georgia,serif;font-size:17px;color:var(--slate);letter-spacing:.5px}
.tired .section-title{margin-top:58px}
.pain-grid{position:absolute;left:160px;top:118px;width:880px;display:grid;grid-template-columns:repeat(3,1fr)}
.pain{height:84px;display:flex;align-items:center;gap:18px;padding:0 22px;font-size:10.5px;line-height:1.45;color:var(--muted);border-right:1px solid var(--line);border-bottom:1px solid var(--line)}
.pain:nth-child(3n){border-right:none}
.pain:nth-child(n+4){border-bottom:none}
.pain svg{flex:0 0 32px}
.pain.on{background:var(--accent);color:var(--white)}

/* steps */
.steps{top:941px;height:328px;background:var(--light)}
.steps .section-title{margin-top:58px}
.step-row{position:absolute;left:160px;top:122px;width:880px;display:grid;grid-template-columns:repeat(4,1fr);gap:14px}
.step{text-align:center;padding:28px 18px 22px;height:210px}
.step h3{font-family:"Cinzel",Georgia,serif;font-size:17px;font-weight:600;color:var(--slate);margin:16px 0 10px}
.step p{font-size:10.5px;line-height:1.6;color:var(--muted)}
.step.on{background:var(--white);box-shadow:0 6px 18px rgba(0,0,0,.12);transform:translateY(-16px)}
.step.on h3{color:var(--accent)}

/* pitch band */
.pitch{top:1269px;height:358px;background:var(--accent)}
.pitch-copy{position:absolute;left:160px;top:128px;width:410px;color:var(--white)}
.pitch-copy::before{content:"";display:block;width:40px;height:2px;background:var(--white);margin-bottom:14px}
.pitch-copy p{font-size:15px;line-height:1.7}
.pitch-copy .btn-pill{border:1.5px solid var(--white);color:var(--white);margin-top:20px}
.growth-ring{position:absolute;left:670px;top:38px;width:346px;height:346px;border-radius:50%;background:var(--accent);border:3px solid var(--white);z-index:2;display:flex;align-items:center;justify-content:center}
.growth-art{width:302px;height:302px;border-radius:50%;background:radial-gradient(circle at 55% 55%,#f7c55a 0%,#f2a93b 22%,#ffffff 48%,#f4f4f4 100%)}

/* reviews */
.reviews{top:1627px;height:510px}
.heading-rule{display:flex;align-items:center;justify-content:center;gap:14px;font-family:"Cinzel",Georgia,serif;font-size:26px;color:var(--slate)}
.heading-rule::before,.heading-rule::after{content:"";width:36px;height:2px;background:var(--accent)}
.reviews .heading-rule{margin-top:76px}
.review-lead{position:absolute;left:160px;top:140px;width:352px;height:310px;border:6px solid #ececec;padding:36px 34px;background:var(--white)}
.review-lead::before{content:"";display:block;width:36px;height:3px;background:var(--accent);margin-bottom:18px}
.review-lead p{font-size:16px;line-height:1.85;color:#555}
.review-card{position:absolute;top:140px;width:241px;height:310px;background:var(--white);box-shadow:0 3px 14px rgba(0,0,0,.14);overflow:hidden}
.review-card blockquote{padding:26px 24px 0;font-size:11.5px;line-height:1.65;color:#555;height:210px;position:relative}
.review-card .qmark{position:absolute;right:22px;font-family:"Cinzel",Georgia,serif;font-size:40px;color:#ccc}
.review-foot{position:absolute;left:0;right:0;bottom:0;height:95px;color:var(--white);text-align:center;font-family:"Cinzel",Georgia,serif;font-size:11.5px;font-weight:600;padding-top:56px;line-height:1.35}
.review-foot span{display:block;font-family:"Open Sans",Arial,sans-serif;font-weight:400;font-size:11px}
.review-foot .badge{position:absolute;left:50%;top:-38px;transform:translateX(-50%);width:76px;height:76px;border-radius:50%}
.card-a{left:536px}.card-a .review-foot{background:var(--accent)}
.card-a .badge{background:#f3d23a;border:4px solid var(--white)}
.card-b{left:799px}.card-b .review-foot{background:var(--slate)}
.card-b .badge{background:linear-gradient(#9a8a7e,#5d534c);border:4px solid var(--white);border-radius:4px}
.review-dots{position:absolute;left:1049px;top:398px;display:flex;flex-direction:column;gap:6px}
.review-dots span{width:5px;height:5px;border-radius:50%;background:#ccc}
.review-dots span:first-child{height:14px;border-radius:3px;background:var(--accent)}

/* contact */
.contact{top:2137px;height:740px;background:var(--light)}
.contact .heading-rule{margin-top:56px}
.contact-panel{position:absolute;left:160px;top:126px;width:880px;height:466px;background:var(--white);overflow:hidden}
.contact-arc{position:absolute;left:-300px;top:0;width:530px;height:466px;border-radius:0 233px 233px 0;background:var(--accent)}
.contact-card{position:absolute;left:77px;top:56px;width:726px;height:348px;background:var(--white);box-shadow:0 4px 18px rgba(0,0,0,.12);display:flex}
.address{width:364px;padding:34px 30px 0 60px;border-right:1px solid var(--line)}
.address h3{font-family:"Cinzel",Georgia,serif;font-size:21px;font-weight:600;color:var(--slate);padding-bottom:14px;border-bottom:1px solid var(--line)}
.addr-row{display:flex;align-items:center;gap:14px;font-size:11px;line-height:1.5;color:#666;margin-top:20px}
.addr-icon{flex:0 0 26px;height:26px;border-radius:3px;background:var(--slate);display:flex;align-items:center;justify-content:center}
.socials{display:flex;margin-top:22px;padding-top:14px;border-top:1px solid var(--line)}
.socials span{width:40px;height:14px;display:flex;justify-content:center;border-right:1px solid var(--line)}
.socials span:last-child{border-right:none}
.socials i{width:8px;height:8px;background:#bbb;border-radius:2px}
.socials span:first-child i{background:var(--accent)}
.contact-form{flex:1;padding:38px 38px 0}
.field-row{display:flex;gap:6px}
.field{flex:1;height:28px;border:1px solid var(--line);font-size:10px;color:#999;padding:0 10px;display:flex;align-items:center;gap:6px;margin-bottom:8px}
.field.tall{height:76px;align-items:flex-start;padding-top:8px}
.field b{font-weight:400;color:#bbb}
.submit{display:block;height:30px;border-radius:15px;background:var(--accent);color:var(--white);text-align:center;font-size:11px;font-weight:700;letter-spacing:1.5px;line-height:30px;margin-top:12px}

/* footer */
.site-footer{top:2720px;height:601px}
.footer-wave{position:absolute;left:0;top:0}
.footer-body{position:absolute;left:0;top:168px;width:1200px;height:433px;background:var(--slate)}
.footer-brand{position:absolute;left:160px;top:268px;width:250px;height:80px;background:var(--white);border-radius:4px 4px 18px 4px;display:flex;align-items:center;justify-content:center}
.footer-about{position:absolute;left:160px;top:368px;width:400px;font-size:11px;line-height:1.75;color:#dfe4e7}
.footer-about a{display:block;margin-top:14px;color:var(--white);font-weight:700;text-decoration:none}
.foot-col{position:absolute;top:270px;color:var(--white)}
.foot-col h4{font-family:"Cinzel",Georgia,serif;font-size:16px;font-weight:600;letter-spacing:.5px;margin-bottom:22px}
.foot-nav a{display:block;color:#e0e5e8;font-size:11px;text-decoration:none;margin-bottom:14px}
.foot-nav a:first-of-type{text-decoration:underline}
.newsletter p{width:208px;font-size:11px;line-height:1.55;color:#dfe4e7}
.news-input{width:206px;height:30px;border-radius:15px;background:var(--white);margin-top:14px;display:flex;align-items:center;gap:8px;padding-left:12px;font-size:10px;color:#999}
.news-btn{display:inline-block;margin-top:10px;background:var(--accent);color:var(--white);border-radius:12px;font-size:10px;font-weight:700;padding:5px 14px}
.copyright{position:absolute;left:160px;top:562px;width:880px;font-size:10.5px;color:#c9d0d4;border-top:1px solid rgba(255,255,255,.12);padding-top:10px}
</style>
</head>
<body>

<header class="hero">
  <div class="hero-bg" role="img" aria-label="Photo of a business team meeting around a table with laptops, darkened"></div>
  <div class="brand-tab"><span class="brand-name">Venture Lanterns</span></div>
  <nav class="main-nav">
    <a class="active" href="#">Home</a><a href="#">Who We Are</a><a href="#">What We Do</a><a href="#">Client Reviews</a><a href="#">Contact Us</a>
  </nav>
  <div class="hero-copy">
    <h1>TECHNOLOGY ADVISORS THAT "GET" BUSINESS.</h1>
    <p>We help you leverage technology to create a competitive advantage.</p>
    <a class="btn-pill" href="#">Schedule Appointment</a>
  </div>
  <div class="outcomes">
    <div class="outcome on">We Get Reducing Time to Decision</div>
    <div class="outcome">We Get Leverage</div>
    <div class="outcome">We Get Standardizing Custom Experience</div>
    <div class="outcome">We Get Scaling Up</div>
    <div class="outcome">We Get Eliminating Bottlenecks</div>
    <div class="outcome">We Get Preparing for Disruption</div>
  </div>
  <div class="hero-arrow left">&#8249;</div>
  <div class="hero-arrow right">&#8250;</div>
  <div class="dots"><span></span><span></span><span></span><span></span></div>
</header>

<section class="tired">
  <h2 class="section-title">Are you tired of "Computer Guys" that...</h2>
  <div class="pain-grid">
    <div class="pain on"><svg width="32" height="32" viewBox="0 0 32 32" fill="none" stroke="#fff" stroke-width="1.6"><rect x="6" y="8" width="20" height="14"/><path d="M10 26h12M12 13l3 3 5-5"/></svg>Don't want to be involved in business strategy.</div>
    <div class="pain"><svg width="32" height="32" viewBox="0 0 32 32" fill="none" stroke="#c77b4f" stroke-width="1.8"><circle cx="16" cy="16" r="12"/><circle cx="12" cy="13" r="1"/><circle cx="20" cy="13" r="1"/><path d="M11 22c3-3 7-3 10 0"/></svg>Give you the excuse, "You never asked."</div>
    <div class="pain"><svg width="32" height="32" viewBox="0 0 32 32" fill="none" stroke="#c77b4f" stroke-width="1.8"><circle cx="6" cy="9" r="1.5"/><circle cx="6" cy="16" r="1.5"/><circle cx="6" cy="23" r="1.5"/><path d="M11 9h17M11 16h17M11 23h17"/></svg>Say "No" but do not give options on how to achieve your business outcome.</div>
    <div class="pain"><svg width="32" height="32" viewBox="0 0 32 32" fill="none" stroke="#c77b4f" stroke-width="1.6"><circle cx="16" cy="13" r="7"/><path d="M13 22h6M14 26h4"/></svg>Recommend technology when a simple process or policy change would have the same effect.</div>
    <div class="pain"><svg width="32" height="32" viewBox="0 0 32 32" fill="none" stroke="#c77b4f" stroke-width="1.6"><path d="M5 27V18h5v9M13 27V13h5v14M21 27V7h5v20"/><path d="M4 27h24"/></svg>Can't explain how a technology will create business value, but insist it is necessary.</div>
    <div class="pain"><svg width="32" height="32" viewBox="0 0 32 32" fill="none" stroke="#c77b4f" stroke-width="1.6"><circle cx="16" cy="16" r="11"/><path d="M16 9v14M19 12h-4a2 2 0 000 4h2a2 2 0 010 4h-4"/></svg>Suggest expensive solutions that are just thrown away, soon after they are deployed.</div>
  </div>
</section>

<section class="steps">
  <h2 class="section-title">The Four Steps to Aligning Technology to your Business Strategy!</h2>
  <div class="step-row">
    <div class="step">
      <svg width="34" height="34" viewBox="0 0 34 34" fill="none" stroke="#555" stroke-width="2.4"><circle cx="14" cy="14" r="9"/><path d="M21 21l9 9"/></svg>
      <h3>Discover</h3><p>Identify what is going on behind the scenes, and create a snapshot of the current infrastructure</p>
    </div>
    <div class="step on">
      <svg width="34" height="34" viewBox="0 0 34 34" fill="none" stroke="#c77b4f" stroke-width="1.8"><circle cx="11" cy="9" r="3"/><circle cx="23" cy="9" r="3"/><path d="M5 20c0-4 3-6 6-6s6 2 6 6M17 20c0-4 3-6 6-6s6 2 6 6M4 22h26v8H4z"/></svg>
      <h3>Prioritize</h3><p>Meet to decide which solutions and policies will have the greatest impact on reaching the companies goals</p>
    </div>
    <div class="step">
      <svg width="34" height="34" viewBox="0 0 34 34" fill="none" stroke="#555" stroke-width="1.8"><circle cx="17" cy="17" r="5"/><circle cx="17" cy="17" r="11" stroke-dasharray="4 3"/></svg>
      <h3>Implement</h3><p>Implement those things that will give the greatest return on investment</p>
    </div>
    <div class="step">
      <svg width="34" height="34" viewBox="0 0 34 34" fill="none" stroke="#555" stroke-width="2.2"><path d="M6 6l22 22M28 6L6 28"/><circle cx="6" cy="6" r="3"/><circle cx="28" cy="28" r="3"/></svg>
      <h3>Maintain</h3><p>Create a system that keeps your technology aligned as strategy adjusts over time</p>
    </div>
  </div>
</section>

<section class="pitch">
  <div class="pitch-copy">
    <p>Computer guys frustrate business leaders because they don't have a business mindset. Venture Lanterns advises on strategy that helps companies apply technology to gain a competitive advantage.</p>
    <a class="btn-pill" href="#">Schedule Appointment</a>
  </div>
  <div class="growth-ring">
    <div class="growth-art" role="img" aria-label="Illustration of a businessman running up a rising orange growth chart"></div>
  </div>
</section>

<section class="reviews">
  <h2 class="heading-rule">Client Reviews</h2>
  <div class="review-lead">
    <p>We get the frustration of working with consultants and experts who don't listen or take the time to understand your company goals and vision. We believe technology should serve your business, not the other way around.</p>
  </div>
  <article class="review-card card-a">
    <blockquote>"The team at Venture Lanterns was instrumental while we grew from 1 location to 6 in just 7 years!"<span class="qmark" style="top:70px">&rdquo;</span></blockquote>
    <div class="review-foot"><i class="badge"></i>- Dale Whitford,<span>Rent-A-Rig</span></div>
  </article>
  <article class="review-card card-b">
    <blockquote>"John and the team at Venture Lanterns are in all our strategy meetings whether or not we think technology will be discussed. And, they have brought great insight to better let us meet our goals."<span class="qmark" style="top:120px">&rdquo;</span></blockquote>
    <div class="review-foot"><i class="badge" role="img" aria-label="Client portrait"></i>- Hank Morrow,<span>Cedar Hill Chapel</span></div>
  </article>
  <div class="review-dots"><span></span><span></span><span></span></div>
</section>

<section class="contact">
  <h2 class="heading-rule">Get in Touch</h2>
  <div class="contact-panel">
    <div class="contact-arc"></div>
    <div class="contact-card">
      <div class="address">
        <h3>Address</h3>
        <div class="addr-row"><span class="addr-icon"><svg width="12" height="14" viewBox="0 0 12 14" fill="none" stroke="#fff" stroke-width="1.4"><path d="M6 13S1 8 1 5a5 5 0 0110 0c0 3-5 8-5 8z"/><circle cx="6" cy="5" r="1.6"/></svg></span>4410 Granite Ridge Parkway, Suite 210 Brookfield, TX 77001</div>
        <div class="addr-row"><span class="addr-icon"><svg width="13" height="13" viewBox="0 0 13 13" fill="none" stroke="#fff" stroke-width="1.4"><path d="M2 1h3l1 3-2 1a7 7 0 004 4l1-2 3 1v3c-6 1-11-4-10-10z"/></svg></span>(555) 014-2290</div>
        <div class="addr-row"><span class="addr-icon"><svg width="13" height="10" viewBox="0 0 13 10" fill="none" stroke="#fff" stroke-width="1.3"><rect x="1" y="1" width="11" height="8"/><path d="M1 1l5.5 4L12 1"/></svg></span>mbellweather@venturelanterns.example</div>
        <div class="socials"><span><i></i></span><span><i></i></span><span><i></i></span><span><i></i></span></div>
      </div>
      <form class="contact-form">
        <div class="field-row"><div class="field"><b>&#9679;</b>Your Name</div><div class="field"><b>&#9993;</b>Your Email</div></div>
        <div class="field"><b>&#9679;</b>Subject</div>
        <div class="field"><b>&#9742;</b>Phone</div>
        <div class="field"><b>&#9679;</b>Address</div>
        <div class="field tall"><b>?</b>Message</div>
        <span class="submit">SUBMIT</span>
      </form>
    </div>
  </div>
</section>

<footer class="site-footer">
  <svg class="footer-wave" width="1200" height="200" viewBox="0 0 1200 200" preserveAspectRatio="none">
    <path d="M0 110 C250 20 450 210 750 130 C950 75 1100 20 1200 0 V200 H0Z" fill="#d9d9d9"/>
    <path d="M0 150 C260 60 470 230 760 160 C960 110 1110 65 1200 45 V200 H0Z" fill="#2f3e47"/>
  </svg>
  <div class="footer-body"></div>
  <div class="footer-brand"><span class="brand-name">Venture Lanterns</span></div>
  <div class="footer-about">Lorem ipsum dolor sit amet, consectetur adipiscing elit, sed do eiusmod tempor incididunt ut labore et dolore magna aliqua. Ut enim ad minim veniam, quis nostrud exercitation ullamco laboris nisi ut aliquip ex ea commodo consequat. Duis aute irure dolor in reprehenderit in voluptate velit esse cillum dolore eu fugiat nulla pariatur.<a href="#">Continue Reading..</a></div>
  <div class="foot-col foot-nav" style="left:611px">
    <h4>Navigation</h4>
    <a href="#">Home</a><a href="#">Who We Are</a><a href="#">What We Do</a><a href="#">Client Reviews</a><a href="#">Contact Us</a>
  </div>
  <div class="foot-col newsletter" style="left:835px">
    <h4>Newsletter</h4>
    <p>Subscribe to our newsletter to keep up with new features &amp; updates from us</p>
    <div class="news-input"><svg width="12" height="9" viewBox="0 0 13 10" fill="none" stroke="#555" stroke-width="1.3"><rect x="1" y="1" width="11" height="8"/><path d="M1 1l5.5 4L12 1"/></svg>Your email address</div>
    <span class="news-btn">SEND</span>
  </div>
  <div class="copyright">© 2018 Venture Lanterns &nbsp;|&nbsp; All rights reserved.</div>
</footer>

</body>
</html>
```